Web Design Project for Kurbly, Chicago

We require a Website designed for a new application. Kurbly, a street parking application which helps car drivers find a street parking spot by offering an ideal path along which to look for parking. This path is calculated by our algorithm based on data (e.g. historical data, baseball games schedule, etc.). Along this path the driver will find a spot and will also save 70% of the search time. Customer we target is reg. between 21 and 45 yo.

We'd like the website to be based on the structure of the attached PDF. Could also be totally different and creative. Open to other options!!!
WE LIKE THIS PAGE: http://www.trelvoqa.de/

We require the following pages designed:
- Main/Home page; with the app demo and maybe a blog implemented on the side
- About page (for company and team)
- Contact page,
- Cool link to get app
- Link for Press/Blog/Socal Media integration and Privacy Policy

Supplied as layered PSD Files

For reference/inspiration only:
One page we like is vornitel.com
Good widget page design: platemerio.com/widgets
Also like their blog: platemerio.com/blog
(Note chirplet integration on the right hand side, as well as Meet the Team video)

Reason: We're starting to get more and more designs and need more time to look into all of them. Very exciting!! Thanks to everybody!

Hi all, we are reviewing the submitted designs and will add some updates to the brief shortly. Sorry about the delay but it's very hard to pick from all those great ideas. Cheers

Target Market(s)

Young, trendy look and interested in tech!

Industry/Entity Type

Parking

Requirements
Must have
• Map should show a path like the app does. Examples to be found under appvista shop Kurbly
Please put the widget as a link and not with a big picture.

```html
<!DOCTYPE html>
<html lang="en">
<head>
<meta charset="utf-8">
<title>Kurbly – Find a street parking spot</title>
<link rel="stylesheet" href="https://fonts.googleapis.com/css2?family=Arvo:wght@700&family=Open+Sans:ital,wght@0,400;0,600;0,700;1,700&family=Quicksand:wght@500;700&display=swap">
<style>
  :root {
    --brand-blue: #0562ab;
    --brand-blue-dark: #034b86;
    --brand-blue-light: #2a86d4;
    --ink: #2b2b2b;
    --ink-soft: #3a3a3a;
    --white: #ffffff;
    --footer: #333333;
    --divider: #c9c9c9;
    --button-grey-top: #f4f4f4;
    --button-grey-bottom: #a9a9a9;
    --field-border: #c8c8c8;
  }
  * { box-sizing: border-box; margin: 0; padding: 0; }
  html, body { width: 1148px; height: 1200px; overflow: hidden; background: var(--white); }
  body { position: relative; font-family: "Open Sans", Arial, sans-serif; color: var(--ink); }

  .site-header { position: absolute; left: 0; top: 0; width: 1148px; height: 174px; }
  .brand { position: absolute; left: 124px; top: 48px; display: flex; align-items: center; gap: 22px; }
  .brand-mark { width: 114px; height: 114px; border-radius: 50%; background: var(--brand-blue); }
  .brand-name { font-family: "Quicksand", sans-serif; font-weight: 700; font-size: 74px; color: var(--ink); letter-spacing: -1px; }

  .main-nav { position: absolute; left: 562px; top: 96px; display: flex; height: 40px; }
  .main-nav a { font-family: "Quicksand", sans-serif; font-weight: 500; font-size: 15.5px; color: var(--ink); text-decoration: none; padding: 0 10px; line-height: 40px; border-left: 1px solid var(--divider); }
  .main-nav a:first-child { border-left: none; }

  .hero-band { position: absolute; left: 0; top: 174px; width: 1148px; height: 279px; background: var(--brand-blue); }
  .hero-devices { position: absolute; left: 117px; top: 194px; width: 591px; height: 364px; background: linear-gradient(135deg, #1c1c1c 0%, #3b3b3b 40%, #e9dfb8 60%, #1c1c1c 100%); border-radius: 18px; }
  .hero-title { position: absolute; left: 729px; top: 232px; width: 300px; font-family: "Arvo", serif; font-weight: 700; font-size: 23px; line-height: 24px; color: var(--white); }
  .btn-try { position: absolute; left: 728px; top: 359px; width: 132px; height: 44px; border-radius: 7px; background: linear-gradient(var(--button-grey-top), var(--button-grey-bottom)); font-style: italic; font-weight: 700; font-size: 25px; color: var(--ink); text-align: center; line-height: 44px; text-decoration: none; }

  .demo-title { position: absolute; left: 115px; top: 580px; font-family: "Arvo", serif; font-weight: 700; font-size: 22px; color: var(--ink-soft); }
  .demo-map { position: absolute; left: 119px; top: 636px; width: 591px; height: 299px; background: linear-gradient(120deg, #ece7de 0%, #f6ee9a 45%, #f3b93c 52%, #ece7de 70%, #e8dfc5 100%); }
  .demo-form label { position: absolute; left: 123px; font-weight: 600; font-size: 17px; color: var(--ink); }
  .demo-form .field { position: absolute; left: 430px; width: 281px; height: 48px; border: 1px solid var(--field-border); background: var(--white); box-shadow: 0 1px 3px rgba(0,0,0,.25); }
  .btn-go { position: absolute; left: 578px; top: 1073px; width: 133px; height: 49px; border-radius: 6px; background: linear-gradient(var(--brand-blue-light), var(--brand-blue)); color: var(--white); font-style: italic; font-weight: 700; font-size: 26px; text-align: center; line-height: 49px; border: none; font-family: "Open Sans", sans-serif; }

  .news-panel { position: absolute; left: 727px; top: 579px; width: 287px; height: 546px; background: linear-gradient(90deg, var(--brand-blue-dark), var(--brand-blue)); box-shadow: 2px 3px 6px rgba(0,0,0,.35); }
  .news-title { position: absolute; left: 11px; top: 10px; font-family: "Arvo", serif; font-weight: 700; font-size: 22px; color: var(--white); }
  .news-list { position: absolute; left: 14px; top: 69px; width: 262px; list-style: none; }
  .news-list li { position: relative; padding-left: 18px; font-size: 12.6px; line-height: 14.4px; color: var(--white); height: 85px; }
  .news-list li::before { content: ""; position: absolute; left: 0; top: 4px; width: 7px; height: 7px; background: var(--white); }
  .btn-learn { position: absolute; left: 147px; top: 490px; width: 133px; height: 33px; border-radius: 6px; background: linear-gradient(var(--button-grey-top), var(--button-grey-bottom)); color: var(--ink-soft); font-weight: 700; font-size: 16px; text-align: center; line-height: 33px; text-decoration: none; }

  .site-footer { position: absolute; left: 0; top: 1165px; width: 1148px; height: 35px; background: var(--footer); display: flex; justify-content: center; gap: 22px; }
  .site-footer a { font-family: "Quicksand", sans-serif; font-weight: 500; font-size: 15px; color: var(--white); text-decoration: none; line-height: 35px; }
</style>
</head>
<body>
  <header class="site-header">
    <div class="brand">
      <span class="brand-mark"></span>
      <span class="brand-name">Kurbly</span>
    </div>
    <nav class="main-nav">
      <a href="#">HOME</a>
      <a href="#">GET KURBLY</a>
      <a href="#">WIDGET</a>
      <a href="#">CAR NAVIGATION</a>
      <a href="#">ABOUT</a>
    </nav>
  </header>

  <section class="hero">
    <div class="hero-band"></div>
    <div class="hero-devices" role="img" aria-label="Two tablets showing a city street map with a highlighted parking search route"></div>
    <h1 class="hero-title">Find a street parking spot with Kurbly and save 70% of the search time.</h1>
    <a class="btn-try" href="#">Try now</a>
  </section>

  <section class="demo">
    <h2 class="demo-title">Try now our demo for free</h2>
    <div class="demo-map" role="img" aria-label="Interactive street map of the downtown area for the demo"></div>
    <form class="demo-form">
      <label style="top:971px">See us in action at this land mark</label>
      <div class="field" style="top:945px"></div>
      <label style="top:1036px">Or pick up any other Scicago address</label>
      <div class="field" style="top:1010px"></div>
      <button class="btn-go" type="button">Go</button>
    </form>
  </section>

  <aside class="news-panel">
    <h2 class="news-title">Blog | Latest News</h2>
    <ul class="news-list">
      <li>Lorem Ipsum is simply dummy text of the printing and typesetting industry. Lorem Ipsum has been the industry's standard dummy text ever since the 1500s...</li>
      <li>Lorem Ipsum is simply dummy text of the printing and typesetting industry. Lorem Ipsum has been the industry's standard dummy text ever since the 1500s...</li>
      <li>Lorem Ipsum is simply dummy text of the printing and typesetting industry. Lorem Ipsum has been the industry's standard dummy text ever since the 1500s...</li>
      <li>Lorem Ipsum is simply dummy text of the printing and typesetting industry. Lorem Ipsum has been the industry's standard dummy text ever since the 1500s.</li>
      <li>Lorem Ipsum is simply dummy text of the printing and typesetting industry. Lorem Ipsum has been the industry's standard dummy text ever since the 1500s.</li>
    </ul>
    <a class="btn-learn" href="#">Learn More</a>
  </aside>

  <footer class="site-footer">
    <a href="#">HOME</a>
    <a href="#">GET KURBLY</a>
    <a href="#">WIDGET</a>
    <a href="#">CAR NAVIGATION</a>
    <a href="#">ABOUT</a>
  </footer>
</body>
</html>
```